IT Services Business Card Design

We require a business card design for an IT services company called RT Code Transit.

We specialize in taking an organisations software and readying it for deployment to new environments (e.g. Nex 3 to Nex 5). This process is termed application packaging. This is not the same as putting things in boxes but I am happy to use boxes as a pun icon ;-) This is our second step in branding, we currently have a new logo and our poor excuse of a website is next to be updated but it contains information on who we are and what we cover at rtcodetransit.example

We are looking for a fun, modern but stylish and professional looking design.

I have attached the logo in multiple formats including vector formats (and the fonts that created the logo if required)
Updates

Thanks to all the designers so far, some great designs in there.  I will be selecting a card design on the deadline date. 

However, there is still time to submit some more designs.  The majority of the ones I have so far are typical simplistic designs that we have all seen before and I have enough of those to choose from now.  If you wish to submit any more designs, please submit somthing unusual to grab our attention.

Target Market(s)

Project executives of large organisations looking for Nexora migrations

Industry/Entity Type

Software

Requirements
Must have
• Want to show company name, contact name, title, main number, contact number, fax number, email address and website address. I do not want to show the address.
Must use the attached logo, retaining the colours in them.

This has to be a double-sided design. I will be using pelby.example and will be selecting their rounded corner business card design.

Their templates and design requirements (sizing etc.) can be found here: http://uk.pelby.example/help/faq/templates-and-guidelines.html

Happy for company name or website to be on either side of the card.

This design has to be original and not used before for another company

Would like to style it around the business colours in the logo
Nice to have
• Pelby.example has an option for multiple card designs to appear on the back. If this is possible in the budget and time you have and you have a design(s) that work with that but carry the same style and theme, that would be nice to see but not necessary.
Should not have
• We do not want to put a postal address on the cards

```html
<!DOCTYPE html>
<html lang="en">
<head>
<meta charset="utf-8">
<title>RT Code Transit – Business Card</title>
<link href="https://fonts.googleapis.com/css2?family=Questrial&family=Open+Sans:ital,wght@1,700&display=swap" rel="stylesheet">
<style>
  :root {
    --backdrop: #e6e6e8;
    --card-front: #ffffff;
    --brand-blue: #3a63b0;
    --navy: #233e7e;
    --back-center: #3a64a8;
    --back-edge: #23407f;
    --ink: #3f3a36;
    --logo-ink: #5a5048;
    --rule: #7a6a58;
    --title: #5a4a3a;
    --silver: #dfe4ec;
    --url: #c9d3e6;
  }
  * { margin: 0; padding: 0; box-sizing: border-box; }
  html, body { width: 1200px; height: 609px; overflow: hidden; }
  body {
    background: var(--backdrop);
    position: relative;
    font-family: "Questrial", sans-serif;
    color: var(--ink);
  }
  .card {
    position: absolute;
    top: 187px;
    width: 418px;
    height: 235px;
    border-radius: 12px;
  }
  .card-front { left: 167px; background: var(--card-front); }
  .card-back {
    left: 615px;
    background: radial-gradient(ellipse 60% 65% at 50% 45%, var(--back-center), var(--back-edge));
  }

  .brand {
    position: absolute;
    display: flex;
    align-items: center;
    gap: 9px;
    font-size: 20px;
    white-space: nowrap;
  }
  .brand-mark {
    width: 24px; height: 24px;
    border-radius: 50%;
    background: var(--brand-blue);
    flex: none;
  }
  .card-front .brand { left: 22px; top: 104px; color: var(--logo-ink); }
  .card-back .brand { left: 50%; top: 101px; transform: translateX(-50%); color: var(--silver); font-size: 22px; }
  .card-back .brand-mark { width: 26px; height: 26px; }

  .divider {
    position: absolute;
    left: 226px; top: 53px;
    width: 1px; height: 128px;
    background: var(--rule);
  }

  .contact { position: absolute; left: 242px; top: 59px; }
  .contact-name {
    font-family: "Open Sans", sans-serif;
    font-style: italic; font-weight: 700;
    font-size: 13.5px; color: var(--navy);
    line-height: 17px;
  }
  .contact-title {
    font-family: "Open Sans", sans-serif;
    font-style: italic; font-weight: 700;
    font-size: 10.5px; color: var(--title);
    line-height: 13px;
  }
  .lines { margin-top: 14px; list-style: none; }
  .lines li {
    display: flex; align-items: center; gap: 6px;
    font-size: 11.5px; height: 18px;
  }
  .lines svg { width: 10px; height: 10px; fill: var(--navy); flex: none; }
  .email { margin-top: 8px; font-size: 10px; }

  .web {
    position: absolute;
    left: 0; right: 0; top: 203px;
    text-align: center;
    font-size: 11px; letter-spacing: 0.3px;
    color: var(--url);
  }
</style>
</head>
<body>
  <section class="card card-front" aria-label="Card front">
    <div class="brand"><span class="brand-mark"></span><span>RT Code Transit</span></div>
    <div class="divider"></div>
    <div class="contact">
      <p class="contact-name">Marcus Delvane</p>
      <p class="contact-title">President</p>
      <ul class="lines">
        <li>
          <svg viewBox="0 0 10 10" aria-label="Phone"><path d="M2 0.5 L4 2.8 L3 4 Q4.2 6 6 7 L7.2 6 L9.5 8 L8.3 9.5 Q4.5 9.5 0.5 1.7 Z"/></svg>
          555-214-7300
        </li>
        <li>
          <svg viewBox="0 0 10 10" aria-label="Fax"><rect x="2.5" y="0.5" width="5" height="3"/><rect x="0.5" y="4" width="9" height="4.5"/><rect x="2.5" y="8" width="5" height="1.5"/></svg>
          555-369-0182
        </li>
        <li>
          <svg viewBox="0 0 10 10" aria-label="Mobile"><rect x="2" y="0" width="6" height="10" rx="0.8"/><rect x="3" y="1.2" width="4" height="6" fill="#fff"/></svg>
          555-695-4410
        </li>
      </ul>
      <p class="email">marcus@rtcodetransit.example</p>
    </div>
  </section>

  <section class="card card-back" aria-label="Card back">
    <div class="brand"><span>RT Code Transit</span><span class="brand-mark"></span></div>
    <p class="web">www.rtcodetransit.example</p>
  </section>
</body>
</html>
```